magcian / mentalist needs flyer desined to send potentisl clients

I need a design that's contemporary, sharp, fun, and professional that will get the attention of whoever receives the flyer very quickly. This is for a tri-fold flyer design.

I've been performing magic for over 40 years. I've performed close-up,
parlor, and stage shows. I've been an Master of Ceremonies, Key Note
Speaker (using magic during presentations to help build on a point or
topic, while keeping the audience entertained and educated on the topic or
topics the client has asked me to focus). I've worked trade shows and
sales training incorporating magic as well. I did private shows in Las
Vegas and L.A. back in the late 90's as well.

I do have website / tobiaskellwoodillusions.example for your to check out.

Target Market(s)

The target audience is corporation Event Planners, Marketing and Sales
managers, casino & hotel entertainment directors, as well as private
businesses looking for unique entertainment options.

Industry/Entity Type

Entertainment Industry

Logo Text

Here are a couple of ideas: your mind is my playground, neural entertainer, professor of mysteries, master of your mind

Requirements
Must have
• I like the black and white look (I think it looks nice, but open to other
• ideas and creativity. Being I'm a magician and mentalist, I'd like for
• both venues to be conveyed somehow. My magic is clean and corporate and family friendly.
Nice to have
• I do have website / tobiaskellwoodillusions.example for your to check out.
• My current business card is attached for review. I'll also attach photos
• I'd like to share, but was unable when I last attempted do sign up. Some
• of the files were too big and I'm not savvy enough to make them smaller,
• but think there might be some potential with a couple.
Should not have
• cartoons or cartoonish graphics. no rabbits, doves, magicians, wands, or top hats.

```html
<!DOCTYPE html>
<html lang="en">
<head>
<meta charset="utf-8">
<title>Tri-fold Flyer – Inside Spread</title>
<link rel="stylesheet" href="https://fonts.googleapis.com/css2?family=Open+Sans:wght@400&family=PT+Sans:wght@700&display=swap">
<style>
  :root {
    --ink: #000000;
    --brand-blue: #1f69ad;
    --paper: #f7f7f7;
    --body-text: #1b1b1b;
    --stage: #d6d8dc;
    --photo-warm: #b48a62;
    --photo-dark: #1c2030;
  }
  html, body {
    margin: 0;
    padding: 0;
    width: 1200px;
    height: 1043px;
    overflow: hidden;
    background: var(--stage);
  }
  .canvas {
    position: relative;
    width: 1200px;
    height: 1043px;
  }
  .spread-art {
    position: absolute;
    left: 0;
    top: 0;
  }
  .copy {
    position: absolute;
    margin: 0;
    font-family: "Open Sans", sans-serif;
    font-size: 17.5px;
    line-height: 21.6px;
    color: var(--body-text);
  }
  .heading {
    position: absolute;
    margin: 0;
    font-family: "PT Sans", sans-serif;
    font-weight: 700;
    color: var(--brand-blue);
  }
  .accent { color: var(--brand-blue); }
  .align-right { text-align: right; }

  .funny-heading { left: 110px; top: 618px; font-size: 25px; }
  .funny-copy { left: 109px; top: 653px; }
  .easy-note { left: 250px; top: 750px; width: 119px; }

  .quote-note { left: 481px; top: 558px; }
  .clean-heading { left: 590px; top: 449px; font-size: 26px; }
  .clean-copy { left: 584px; top: 488px; }

  .guests-copy { left: 900px; top: 704px; width: 197px; }
</style>
</head>
<body>
<main class="canvas">
  <svg class="spread-art" width="1200" height="1043" viewBox="0 0 1200 1043" aria-hidden="false">
    <defs>
      <clipPath id="sheet">
        <rect x="75" y="156" width="1044" height="738"/>
      </clipPath>
      <linearGradient id="photo-tone-warm" x1="0" y1="0" x2="1" y2="1">
        <stop offset="0" stop-color="#c9a57a"/>
        <stop offset="1" stop-color="#6b4a36"/>
      </linearGradient>
      <linearGradient id="photo-tone-stage" x1="0" y1="0" x2="1" y2="1">
        <stop offset="0" stop-color="#2a2e44"/>
        <stop offset="1" stop-color="#11131d"/>
      </linearGradient>
    </defs>

    <g class="sheet" clip-path="url(#sheet)">
      <!-- panel grounds -->
      <rect class="panel-black" x="75" y="156" width="1044" height="738" fill="var(--ink)"/>
      <rect class="panel-blue" x="422" y="156" width="348" height="738" fill="var(--brand-blue)"/>

      <!-- white fields -->
      <polygon class="field-left" points="75,425 75,894 544,894" fill="var(--paper)"/>
      <polygon class="field-centre" points="705,290 1055,640 705,990 355,640" fill="var(--paper)"/>
      <polygon class="field-right" points="1119,620 1119,894 845,894" fill="var(--paper)"/>

      <!-- photo diamonds -->
      <polygon role="img" aria-label="Photo: magician performing close-up card magic for a guest at a table" points="248,250 393,395 248,540 103,395" fill="url(#photo-tone-warm)"/>
      <polygon role="img" aria-label="Photo: magician performing a rope routine on stage with a volunteer" points="597,117 742,262 597,407 452,262" fill="url(#photo-tone-stage)"/>
      <polygon role="img" aria-label="Photo: magician performing with a red silk for a seated guest at a corporate event" points="945,185 1090,330 945,475 800,330" fill="url(#photo-tone-warm)"/>
      <polygon role="img" aria-label="Photo: guest reacting as the magician performs at a banquet table" points="915,530 1025,640 915,750 805,640" fill="url(#photo-tone-warm)"/>

      <!-- white accent squares -->
      <g class="accent-squares-white" fill="var(--paper)">
        <polygon points="109,172 121,184 109,196 97,184"/>
        <polygon points="127,191 140,204 127,217 114,204"/>
        <polygon points="109,210 121,222 109,234 97,222"/>
        <polygon points="183,233 216,266 183,299 150,266"/>
        <polygon points="142,274 175,307 142,340 109,307"/>
        <polygon points="298,214 331,247 298,280 265,247"/>
        <polygon points="327,268 349,290 327,312 305,290"/>
        <polygon points="380,166 402,188 380,210 358,188"/>
        <polygon points="364,206 378,220 364,234 350,220"/>
        <polygon points="399,206 413,220 399,234 385,220"/>
        <polygon points="365,437 398,470 365,503 332,470"/>
        <polygon points="322,477 390,545 322,613 254,545"/>
        <polygon points="825,204 835,214 825,224 815,214"/>
        <polygon points="808,222 818,232 808,242 798,232"/>
        <polygon points="826,238 850,262 826,286 802,262"/>
        <polygon points="806,280 816,290 806,300 796,290"/>
        <polygon points="789,295 799,305 789,315 779,305"/>
        <polygon points="1022,426 1084,488 1022,550 960,488"/>
      </g>

      <!-- blue / black accent squares -->
      <g class="accent-squares-blue" fill="var(--brand-blue)">
        <polygon points="708,330 720,342 708,354 696,342"/>
        <polygon points="734,356 754,376 734,396 714,376"/>
        <polygon points="770,393 770,457 738,425"/>
        <polygon points="422,631 455,664 422,697"/>
        <polygon points="610,817 643,850 610,883 577,850"/>
      </g>
      <g class="accent-squares-black" fill="var(--ink)">
        <polygon points="770,393 802,425 770,457"/>
        <polygon points="422,631 422,697 389,664"/>
      </g>
    </g>
  </svg>

  <h2 class="heading funny-heading">I’m funny!</h2>
  <p class="copy funny-copy">I make sure you’re<br>comfortable with<br>every step in the<br>process of dealing<br>with me. From<br>booking to follow-<br>up you’ll be<br>&nbsp;happy.</p>
  <p class="copy accent align-right easy-note">Doing<br>business<br>with me is<br>easy.</p>

  <p class="copy accent quote-note">I often tell<br>people, “If<br>magic<br>really<br>existed,<br>this is<br>what it<br>would<br>look like.”</p>
  <h2 class="heading clean-heading">I work clean</h2>
  <p class="copy clean-copy">&nbsp;I pride myself on<br>building relation-<br>ships with my<br>customers, so I’m<br>not happy unless<br>you’re happy. I<br>guarantee your<br>guests will have a<br>great time and<br>will thank you for<br>having me there.<br>again and again.</p>

  <p class="copy align-right guests-copy">Your<br>guests<br>will experi-<br>ence magic<br>that looks like<br>magic. Their jaws<br>will drop and they<br>will literally gasp in</p>
</main>
</body>
</html>
```